Visitenkarten- und Briefpapier Design - Logo vorhanden!
Zielgruppe
Wir sind eine Projektentwicklungs GmbH die Grundstücke kauft, projektiert und wieder verkauft. Eine zukünftige GmbH ist für den Innenausbau von neuen Häusern (EFH,DHH,MFH) gedacht. Wir sind ebenfalls für den Vertrieb von Häusern tätig.
Unsere Zielgruppe sind Endkunden im Immobilienbereich die Grundstücke und/oder Häuser bis Schlüsselfertig kaufen möchten, sowie Grundstückseigentümer die verkaufen wollen.
Wir benötigen Visitenkarten UND Briefpapier.
Aufgabenstellung
Bitte vorhandenes Logo verwenden.
Briefpapier:
Es soll ein ansprechendes modernes Design sein. Wir lassen uns gerne überraschen und versuchen schnellstmöglich Feedback zu geben.
Visitenkarte:
Es soll ein ansprechendes modernes Design sein. Die Visitenkarte bitte mit 2 Seiten, auf der Rückseite könnten wir uns das Dunkle ZERANT Logo sehr gut vorstellen (nur Logo).

```html
<!DOCTYPE html>
<html lang="de">
<head>
<meta charset="utf-8">
<title>ZERANT Briefpapier und Visitenkarten</title>
<link href="https://fonts.googleapis.com/css2?family=EB+Garamond:wght@400;600&display=swap" rel="stylesheet">
<style>
  :root {
    --navy: #1d202b;
    --ink: #22252f;
    --stone: #dfe0da;
    --paper: #ffffff;
  }
  html, body { margin: 0; padding: 0; overflow: hidden; background: var(--paper); }
  .sheet {
    position: relative; width: 849px; height: 1200px; overflow: hidden;
    background: var(--paper);
    font-family: "EB Garamond", Georgia, serif; color: var(--ink);
  }
  .frame { position: absolute; inset: 0; width: 849px; height: 1200px; }
  .art-area { position: absolute; }
  .letter-art {
    left: 0; top: 820px; width: 849px; height: 380px;
    background: linear-gradient(to bottom, rgba(223,224,218,0) 0%, var(--stone) 100%);
  }
  .card-art {
    left: 544px; top: 620px; width: 226px; height: 116px;
    background: linear-gradient(to bottom, rgba(223,224,218,0) 0%, var(--stone) 100%);
  }
  .t { position: absolute; margin: 0; white-space: nowrap; line-height: 1; }
  .header-title { left: 77px; top: 111px; font-size: 28px; color: var(--paper); }
  .brand-header { left: 663px; top: 108px; font-size: 29px; color: var(--paper); letter-spacing: 0.5px; }
  .sender-name { left: 663px; top: 156px; font-size: 19px; font-weight: 600; }
  .sender-line { font-size: 11px; }
  .label-col { left: 663px; }
  .value-col { left: 724px; }
  .card-brand { font-size: 18px; color: var(--paper); top: 410px; }
  .card-name { left: 294px; font-size: 18.5px; font-weight: 600; }
  .card-role { left: 294px; top: 539px; font-size: 11px; }
  .card-line { font-size: 10.5px; }
  .card-label { left: 294px; }
  .card-value { left: 354px; }
  .footer { left: 125px; font-size: 11px; text-transform: uppercase; color: #333640; }
</style>
</head>
<body>
<div class="sheet">
  <div class="art-area letter-art" role="img" aria-label="Dekorative Dachflächen in hellem Steingrau am unteren Briefbogenrand"></div>

  <svg class="frame" viewBox="0 0 1624 2296" preserveAspectRatio="none" aria-hidden="true">
    <defs>
      <filter id="cardShadow" x="-10%" y="-10%" width="130%" height="130%">
        <feDropShadow dx="6" dy="10" stdDeviation="8" flood-color="#000" flood-opacity="0.35"/>
      </filter>
    </defs>
    <rect x="0" y="72" width="1624" height="207" fill="#1d202b"/>
    <g filter="url(#cardShadow)">
      <rect x="518" y="666" width="432" height="742" fill="#fff"/>
    </g>
    <rect x="518" y="718" width="432" height="120" fill="#1d202b"/>
    <g filter="url(#cardShadow)">
      <rect x="1040" y="666" width="432" height="742" fill="#fff"/>
    </g>
    <rect x="1040" y="718" width="432" height="120" fill="#1d202b"/>
  </svg>

  <div class="art-area card-art" role="img" aria-label="Dekorative Dachflächen in hellem Steingrau auf der Kartenrückseite"></div>

  <p class="t header-title">Imobilienverwaltung</p>
  <p class="t brand-header">ZERANT</p>

  <p class="t sender-name">ZERANT</p>
  <p class="t sender-line label-col" style="top:179px">Imobilienverwaltung</p>
  <p class="t sender-line label-col" style="top:206px">Musterstraße</p>
  <p class="t sender-line value-col" style="top:206px">123</p>
  <p class="t sender-line label-col" style="top:220px">Musterstadt</p>
  <p class="t sender-line value-col" style="top:220px">12345</p>
  <p class="t sender-line label-col" style="top:248px">Telefon:</p>
  <p class="t sender-line value-col" style="top:248px">+49 (0) 123 456789</p>
  <p class="t sender-line label-col" style="top:261px">Email:</p>
  <p class="t sender-line value-col" style="top:261px">info@zerant.com</p>
  <p class="t sender-line label-col" style="top:275px">Web:</p>
  <p class="t sender-line value-col" style="top:275px">www.zerant.com</p>
  <p class="t sender-line label-col" style="top:302px">Steuernr.:</p>
  <p class="t sender-line value-col" style="top:302px">123/456/789</p>

  <p class="t card-brand" style="left:407px">ZERANT</p>
  <p class="t card-name" style="top:497px">Max</p>
  <p class="t card-name" style="top:520px">Mustermann</p>
  <p class="t card-role">Musterposition</p>
  <p class="t card-line card-label" style="top:594px">Telefon:</p>
  <p class="t card-line card-value" style="top:594px">+49 (0) 123 456789</p>
  <p class="t card-line card-label" style="top:608px">Email:</p>
  <p class="t card-line card-value" style="top:608px">m.mustermann@zerant.com</p>
  <p class="t card-line card-label" style="top:622px">Web:</p>
  <p class="t card-line card-value" style="top:622px">www.zerant.com</p>

  <p class="t card-brand" style="left:680px">ZERANT</p>

  <p class="t footer" style="top:1129px">Mustertext | Firmenname | Geschäftsführung M. Muster | Firmen Steuernummer | Firmen Ust-ID-Nr</p>
  <p class="t footer" style="top:1143px">Musterbankverbindung 1 | BLZ 123 456 78 | Konto-Nr. 1 234 567 &nbsp;| IBAN 123 456 789 123 456 789 | BIC Muster</p>
</div>
</body>
</html>
```